Income Tax and Accounting Brochure

I need a brochure using my new logo (file attached). I do tax work and accounting work. I am an EA (QDX Enrolled Agent - logo attached) and would like this incorporated into the brochure. I also have a MSA in Accounting. Please incorporate the text that I have provided in the brochure.

Target Market(s)

Tax Clients - both business and individuals

Industry/Entity Type

Accounting

Colors
0054AA
0677BA
7BADD7
CADEEF
E8F1F8

Requirements
Must have
• Use my logo and the QDX EA file in the brochure
Nice to have
• I would like to see a brochure that I can customize with my own text if possible.

```html
<!DOCTYPE html>
<html lang="en">
<head>
<meta charset="utf-8">
<title>Northvale Accounting &amp; Consulting Brochure</title>
<link href="https://fonts.googleapis.com/css2?family=Rubik:ital,wght@0,400;0,500;0,700;1,400&display=swap" rel="stylesheet">
<style>
:root{
  --stage:#d4d5d7;
  --ink:#141820;
  --blue:#1554a8;
  --red:#c0202f;
  --white:#ffffff;
  --text-dark:#1a1a1a;
  --text-light:#f2f2f2;
}
*{margin:0;padding:0;box-sizing:border-box}
html,body{width:902px;height:1200px;overflow:hidden}
body{background:var(--stage);font-family:"Rubik",Arial,sans-serif;position:relative}
.spread{position:absolute;left:93px;width:707px;height:500px;box-shadow:3px 4px 8px rgba(0,0,0,.45);overflow:hidden}
.spread--cover{top:73px}
.spread--inside{top:630px}
.page{position:absolute;top:0;width:353.5px;height:500px;overflow:hidden}
.page--left{left:0}
.page--right{left:353.5px}
.dark{background:var(--ink);color:var(--text-light)}
.brand{position:absolute;display:flex;align-items:center;gap:9px}
.brand__dot{width:14px;height:14px;border-radius:50%;background:var(--blue)}
.brand__name{color:var(--blue);font-weight:500;font-size:15px;line-height:1.2;letter-spacing:.5px;text-transform:uppercase}
.cover-back .brand{left:38px;top:232px}
.cover-front .brand{left:24px;top:48px}
.contact{position:absolute;left:0;right:0;bottom:14px;text-align:center;font-size:8px}
.cityscape{position:absolute;left:0;top:110px;width:353.5px;height:390px;
  background:radial-gradient(circle at 55% 40%,#3a8fc4 0%,#1b3d6d 38%,#1c2230 70%),#1c2230}
.about{position:absolute;left:25px;top:24px;width:162px}
.about h2{font-size:12.5px;font-weight:500;color:var(--white);line-height:1.2}
.about .role{font-style:italic;font-size:9px;margin-bottom:11px}
.about p{font-size:8px;line-height:1.27;margin-bottom:10px}
.band{position:absolute;left:0;width:353.5px;height:29px;display:flex;align-items:center;color:var(--white);font-weight:500;font-size:14.5px}
.band--blue{background:var(--blue)}
.band--red{background:var(--red)}
.band--center{justify-content:center}
.band--indent{padding-left:19px}
.white-panel{position:absolute;left:0;top:286px;width:353.5px;height:214px;background:var(--white);color:var(--text-dark)}
.ribbon{position:absolute;left:0;top:20px;width:212px;height:25px;background:var(--red);color:var(--white);
  font-size:9.5px;font-weight:700;display:flex;align-items:center;padding-left:20px;gap:13px;
  clip-path:polygon(0 0,100% 0,94% 100%,0 100%)}
.ribbon::before{content:"";width:6px;height:6px;border-radius:50%;background:var(--white)}
.white-panel .body{position:absolute;left:20px;top:66px;width:284px}
.white-panel p{font-size:8px;line-height:1.27;margin-bottom:11px}
.gets{position:absolute;left:0;top:0;width:353.5px;height:257px;background:var(--white);color:var(--text-dark)}
.gets .band{top:0;height:30px;font-size:13.5px}
.gets ul{list-style:none;position:absolute;left:49px;top:55px;width:256px}
.gets li{position:relative;padding-left:23px;font-size:8px;line-height:1.27;margin-bottom:10px}
.gets li svg{position:absolute;left:0;top:-1px;width:14px;height:14px}
.books{position:absolute;left:0;top:257px;width:353.5px;height:243px}
.books .band{top:0;height:29px;font-size:13.5px}
.books p{position:absolute;left:103px;top:72px;width:168px;font-size:8px;line-height:1.27}
</style>
</head>
<body>

<section class="spread spread--cover">
  <div class="page page--left dark cover-back">
    <div class="brand"><span class="brand__dot"></span><span class="brand__name">Northvale Accounting<br>&amp; Consulting, LLC</span></div>
    <p class="contact">Contact&nbsp;&nbsp; 555.010.4821 | www.northvaleacct.com</p>
  </div>
  <div class="page page--right dark cover-front">
    <div class="brand"><span class="brand__dot"></span><span class="brand__name">Northvale Accounting<br>&amp; Consulting, LLC</span></div>
    <div class="cityscape" role="img" aria-label="Night city skyline photograph with light trails, framed by a large blue and red sweeping curve"></div>
  </div>
</section>

<section class="spread spread--inside">
  <div class="page page--left dark">
    <div class="about">
      <h2>About Marian D Holloway,</h2>
      <p class="role">MSA EA (Principal)</p>
      <p>I have a Masters' Degree in accounting and am an QDX Enrolled Agent. I am also a LedgerBooks Advanced Certified Consultant in both the online and desktop products including Enterprise and Point of Sale. I provide individual and small business tax services, Accounting, bookkeeping, QDX representation, insurance audit representation, business license assistance and more.</p>
      <p>I have experience working with a wide variety of clients from the point where they first decide they want to start a business. They are often unsure about what to do first- I have a lot of experience to offer you.</p>
    </div>
    <div class="band band--blue band--indent" style="top:257px">What a joy it is to watch success in action!</div>
    <div class="white-panel">
      <div class="ribbon">Tax Preparation – why hire us</div>
      <div class="body">
        <p>Preparing your own income tax return can be a task that leaves you with more questions than answers. According to a study released by the Federal Review Bureau last year, most taxpayers (77% of 71 million taxpayers) believe they benefited from using a professional tax preparer.</p>
        <p>Whether we like it or not, today's tax laws are so complicated that filing a relatively simple return can be confusing. It is just too easy to overlook deductions and credits to which you are entitled. Even if you use a computer software program there's no substitute for the assistance of an experienced tax professional.</p>
      </div>
    </div>
  </div>

  <div class="page page--right dark">
    <div class="gets">
      <div class="band band--blue band--center">Here's what your get...</div>
      <ul>
        <li><svg viewBox="0 0 14 14" aria-hidden="true"><rect x="1" y="2" width="11" height="11" fill="none" stroke="#c0202f" stroke-width="1.2"/><path d="M3 7l3 4 7-10" fill="none" stroke="#1554a8" stroke-width="2"/></svg>Your tax return will be checked and rechecked by our computer software identifying potential problems the QDX may look at more closely and reviewing the math to limit QDX contacts.</li>
        <li><svg viewBox="0 0 14 14" aria-hidden="true"><rect x="1" y="2" width="11" height="11" fill="none" stroke="#c0202f" stroke-width="1.2"/><path d="M3 7l3 4 7-10" fill="none" stroke="#1554a8" stroke-width="2"/></svg>Your tax return can be filed electronically so you will get a refund back quicker.</li>
        <li><svg viewBox="0 0 14 14" aria-hidden="true"><rect x="1" y="2" width="11" height="11" fill="none" stroke="#c0202f" stroke-width="1.2"/><path d="M3 7l3 4 7-10" fill="none" stroke="#1554a8" stroke-width="2"/></svg>Our staff will show you how to adjust your payroll withholding to get more money back each week. Why give the QDX an interest free loan for up to 16 months.</li>
        <li><svg viewBox="0 0 14 14" aria-hidden="true"><rect x="1" y="2" width="11" height="11" fill="none" stroke="#c0202f" stroke-width="1.2"/><path d="M3 7l3 4 7-10" fill="none" stroke="#1554a8" stroke-width="2"/></svg>We will show you potential deductions to limit your tax liability for next year. In addition, we will give you a sheet of commonly overlooked deductions to limit the following year's tax liability.</li>
      </ul>
    </div>
    <div class="books">
      <div class="band band--red band--center">Books a Mess: No Problem!</div>
      <p>If you own a small business and haven't kept up your bookkeeping, don't worry. We can help you. We'll prepare your bookkeeping for the year, prepare a full Schedule C, as well as your personal income tax return. Then we'll help you set up an easy system that allows you to keep your books in tip-top shape next year.</p>
    </div>
  </div>
</section>

</body>
</html>
```